Bright Towns Alliance PowerPoint Design Template and Sample Deck

The Bright Towns Alliance is an international organization that seeks to improve the livability, workability and sustainability of the world’s cities.
We seek a versatile PowerPoint design template with 10 slide types plus a “self-documenting” sample deck. Your design will be used in keynote speeches and workshops around the world.
After the contest is completed, we will ask the winning designer to add 10-20 additional slide types for $75 per slide. We also seek a long-term relationship whereby we can request “custom” slides and/or ask the designer to touch up the slides we build to make them better.
FILES. We have uploaded several files:
2. PALETTE. Shows our official colors.
3 LOGOS. Several individual files with different variations of our logo. Some with our motto, some without.
2. SAMPLE SLIDES. Because we were unable to successfully upload our sample deck, we are making it available via this FileCrate link:
https://www.filecrate-example.net/s/q7mrk2tzw9hdn4e/The%20Bright%20Towns%20Alliance%20Design%20Contest%20Notes.docx?dl=0
Target Market(s)
Mayors, department heads, CIOs, senior executives from technology companies
Industry/Entity Type
Information Technology
Colors
Designer to choose colors to be used in the design.
Requirements
Must have
- Please see uploaded Word document for requirements, nice to haves and should not haves and uploaded palette for color preferences.
Nice to have
- see above
Should not have
- see above

```html
<!DOCTYPE html>
<html lang="en">
<head>
<meta charset="utf-8">
<title>Bright Towns Alliance – Four Pillars</title>
<link rel="stylesheet" href="https://fonts.googleapis.com/css2?family=Arimo:wght@400&family=Carlito:wght@400;700&display=swap">
<style>
  :root {
    --bg-deep: #0a2450;
    --bg-mid: #0d4a8c;
    --bg-edge: #0a2a5c;
    --glow: rgba(110, 150, 205, 0.28);
    --ring-navy: #0b2a57;
    --white: #ffffff;
    --orange: #f5941f;
    --rule-light: rgba(170, 200, 235, 0.65);
    --rule-orange: #d9791a;
    --badge: #0f3f7a;
  }
  * { margin: 0; padding: 0; box-sizing: border-box; }
  html, body { width: 1200px; height: 675px; overflow: hidden; }
  body {
    font-family: "Carlito", "Calibri", sans-serif;
    color: var(--white);
  }
  .slide {
    position: relative;
    width: 1200px;
    height: 675px;
    overflow: hidden;
    background: radial-gradient(ellipse 75% 90% at 45% 50%, var(--bg-mid) 0%, var(--bg-edge) 70%, var(--bg-deep) 100%);
  }
  .backdrop-glow {
    position: absolute;
    left: 410px;
    top: 0;
    width: 790px;
    height: 440px;
    background: radial-gradient(ellipse 50% 50% at 50% 45%, var(--glow) 0%, rgba(110, 150, 205, 0.12) 60%, rgba(110, 150, 205, 0) 100%);
  }
  .slide-title {
    position: absolute;
    left: 65px;
    top: 53px;
    font-family: "Arimo", "Arial", sans-serif;
    font-weight: 400;
    font-size: 49px;
    line-height: 60px;
    white-space: nowrap;
  }
  .pillar {
    position: absolute;
    top: 0;
    width: 262px;
    height: 675px;
  }
  .pillar-badge {
    position: absolute;
    left: 131px;
    top: 218px;
    width: 140px;
    height: 140px;
    margin: -70px 0 0 -70px;
    border-radius: 50%;
    background: var(--ring-navy);
    box-shadow: 4px 6px 8px rgba(0, 0, 0, 0.35);
    display: flex;
    align-items: center;
    justify-content: center;
  }
  .pillar-badge-face {
    width: 126px;
    height: 126px;
    border-radius: 50%;
    background: var(--white);
    display: flex;
    align-items: center;
    justify-content: center;
  }
  .pillar-figure {
    width: 96px;
    height: 62px;
    border-radius: 6px;
    background: linear-gradient(180deg, #f7a33d, var(--orange));
  }
  .pillar-rule {
    position: absolute;
    left: 0;
    top: 304px;
    width: 262px;
    height: 1px;
    background: var(--rule-light);
  }
  .pillar-heading {
    position: absolute;
    left: 0;
    top: 322px;
    width: 262px;
    text-align: center;
    font-weight: 700;
    font-size: 20.5px;
    line-height: 27px;
  }
  .pillar-callout {
    position: absolute;
    left: 0;
    top: 396px;
  }
  .pillar-text {
    position: absolute;
    left: 15px;
    top: 440px;
    width: 232px;
    text-align: center;
    font-size: 16.2px;
    line-height: 21px;
  }
  .divider {
    position: absolute;
    top: 434px;
    width: 1px;
    height: 185px;
    background: linear-gradient(180deg, var(--rule-orange), rgba(217, 121, 26, 0.25));
  }
  .page-number {
    position: absolute;
    left: 1090px;
    top: 624px;
    width: 50px;
    height: 50px;
    border-radius: 50%;
    background: var(--badge);
    font-family: "Arimo", "Arial", sans-serif;
    font-size: 14px;
    display: flex;
    align-items: center;
    justify-content: center;
  }
</style>
</head>
<body>
<main class="slide">
  <div class="backdrop-glow" role="img" aria-label="Faint decorative backdrop of two overlapping speech bubbles"></div>

  <h1 class="slide-title">Lorem Ipsum is simply dummy</h1>

  <section class="pillar" style="left:60px">
    <div class="pillar-badge"><div class="pillar-badge-face"><div class="pillar-figure" role="img" aria-label="Orange silhouette of two colleagues working at a computer desk"></div></div></div>
    <div class="pillar-rule"></div>
    <h2 class="pillar-heading">Lorem Ipsum is simply<br>dummy</h2>
    <svg class="pillar-callout" width="262" height="26" viewBox="0 0 262 26" aria-hidden="true"><polyline points="0,7 206,7 209,23 224,7 262,7" fill="none" stroke="var(--rule-orange)" stroke-width="1.2"/></svg>
    <p class="pillar-text">Lorem Ipsum is simply dummy text of the printing and typesetting industry. Lorem Ipsum has been the industry's standard dummy text ever since the 1500s</p>
  </section>

  <section class="pillar" style="left:334px">
    <div class="pillar-badge"><div class="pillar-badge-face"><div class="pillar-figure" role="img" aria-label="Orange silhouette of shoppers carrying bags"></div></div></div>
    <div class="pillar-rule"></div>
    <h2 class="pillar-heading">Lorem Ipsum is simply<br>dummy</h2>
    <svg class="pillar-callout" width="262" height="26" viewBox="0 0 262 26" aria-hidden="true"><polyline points="0,7 206,7 209,23 224,7 262,7" fill="none" stroke="var(--rule-orange)" stroke-width="1.2"/></svg>
    <p class="pillar-text">Lorem Ipsum is simply dummy text of the printing and typesetting industry. Lorem Ipsum has been the industry's standard dummy text ever since the 1500s</p>
  </section>

  <section class="pillar" style="left:607px">
    <div class="pillar-badge"><div class="pillar-badge-face"><div class="pillar-figure" role="img" aria-label="Orange silhouette of three people meeting at a table"></div></div></div>
    <div class="pillar-rule"></div>
    <h2 class="pillar-heading">Lorem Ipsum is simply<br>dummy</h2>
    <svg class="pillar-callout" width="262" height="26" viewBox="0 0 262 26" aria-hidden="true"><polyline points="0,7 206,7 209,23 224,7 262,7" fill="none" stroke="var(--rule-orange)" stroke-width="1.2"/></svg>
    <p class="pillar-text">Lorem Ipsum is simply dummy text of the printing and typesetting industry. Lorem Ipsum has been the industry's standard dummy text ever since the 1500s</p>
  </section>

  <section class="pillar" style="left:880px">
    <div class="pillar-badge"><div class="pillar-badge-face"><div class="pillar-figure" role="img" aria-label="Orange silhouette of people walking in a line"></div></div></div>
    <div class="pillar-rule"></div>
    <h2 class="pillar-heading">Lorem Ipsum is simply<br>dummy</h2>
    <svg class="pillar-callout" width="262" height="26" viewBox="0 0 262 26" aria-hidden="true"><polyline points="0,7 206,7 209,23 224,7 262,7" fill="none" stroke="var(--rule-orange)" stroke-width="1.2"/></svg>
    <p class="pillar-text">Lorem Ipsum is simply dummy text of the printing and typesetting industry. Lorem Ipsum has been the industry's standard dummy text ever since the 1500s</p>
  </section>

  <div class="divider" style="left:329px"></div>
  <div class="divider" style="left:601px"></div>
  <div class="divider" style="left:873px"></div>

  <div class="page-number">5</div>
</main>
</body>
</html>
```